Ridgeway Sparks Business cards

We require somebody to design business cards for our new business.

Target Market(s)

Mining, haulage and civil.

Industry/Entity Type

Auto electrician in mining industry

Contact Information for Business Card

ABN, business email address, mobile number.

Colors
00AB8E
00BBA5
67D7C9
C6EFE9
E9F9F6

Requirements
Must have
• Services I offer: Breakdowns, Field Service, A/C Systems, Machine rewires, mine site vehicle fit outs

```html
<!DOCTYPE html>
<html lang="en">
<head>
<meta charset="utf-8">
<title>Ridgeway Sparks — Business Cards</title>
<link href="https://fonts.googleapis.com/css2?family=Montserrat:wght@400;500;600;700&display=swap" rel="stylesheet">
<style>
  :root {
    --page-bg: #2a2a2c;
    --card-bg: #1c1c1e;
    --teal: #3ec8bd;
    --white: #f2f2f2;
    --mark-grey: #4a4a4d;
  }
  * { box-sizing: border-box; margin: 0; padding: 0; }
  html, body {
    width: 1200px; height: 874px; overflow: hidden;
    background: var(--page-bg);
    font-family: "Montserrat", sans-serif;
  }
  .card {
    position: absolute;
    left: 290px;
    width: 620px; height: 378px;
    background: var(--card-bg);
    border-radius: 22px;
    box-shadow: 0 10px 30px rgba(0,0,0,.45);
  }
  .card--front { top: 40px; }
  .card--back { top: 456px; }

  .front-mark {
    position: absolute; inset: 0;
    display: flex; align-items: center; justify-content: center;
    gap: 14px;
  }
  .front-mark .mark-square {
    width: 26px; height: 26px; background: var(--mark-grey);
  }
  .front-mark .mark-name {
    font-weight: 700; font-size: 34px; color: var(--mark-grey);
    letter-spacing: 1px; text-transform: uppercase;
  }

  .back-brand {
    position: absolute; left: 36px; top: 120px; width: 230px;
    display: flex; align-items: center; gap: 10px;
  }
  .back-brand .mark-square { width: 18px; height: 18px; background: var(--teal); flex: none; }
  .back-brand .mark-name {
    font-weight: 700; font-size: 24px; line-height: 1.1; color: var(--teal);
    text-transform: uppercase;
  }

  .divider {
    position: absolute; left: 290px; top: 56px;
    width: 2px; height: 190px; background: var(--teal);
  }

  .contact { position: absolute; left: 318px; top: 58px; color: var(--white); }
  .contact .person-name { font-weight: 600; font-size: 28px; color: var(--teal); }
  .contact .person-role { font-size: 16px; margin-top: 2px; }
  .contact .abn { font-size: 16px; margin-top: 22px; }
  .contact-list { list-style: none; margin-top: 18px; }
  .contact-list li {
    display: flex; align-items: center; gap: 10px;
    font-size: 16px; line-height: 26px;
  }
  .contact-list svg { width: 14px; height: 14px; fill: var(--white); flex: none; }

  .services {
    position: absolute; left: 16px; right: 16px; top: 278px; text-align: center;
  }
  .services .services-title { font-weight: 700; font-size: 18px; color: var(--teal); }
  .services .services-list {
    font-size: 14px; color: var(--white); margin-top: 6px; white-space: nowrap;
  }
</style>
</head>
<body>
  <section class="card card--front" aria-label="Business card front">
    <div class="front-mark">
      <span class="mark-square"></span>
      <span class="mark-name">Ridgeway Sparks</span>
    </div>
  </section>

  <section class="card card--back" aria-label="Business card back">
    <div class="back-brand">
      <span class="mark-square"></span>
      <span class="mark-name">Ridgeway Sparks</span>
    </div>

    <div class="divider"></div>

    <div class="contact">
      <p class="person-name">Daniel Harcourt</p>
      <p class="person-role">Managing Director</p>
      <p class="abn">ABN# 123 45678</p>
      <ul class="contact-list">
        <li>
          <svg viewBox="0 0 24 24"><path d="M6.6 10.8a15.1 15.1 0 0 0 6.6 6.6l2.2-2.2a1 1 0 0 1 1-.25 11.4 11.4 0 0 0 3.6.57 1 1 0 0 1 1 1V20a1 1 0 0 1-1 1A17 17 0 0 1 3 4a1 1 0 0 1 1-1h3.5a1 1 0 0 1 1 1c0 1.25.2 2.45.57 3.57a1 1 0 0 1-.25 1z"/></svg>
          123 456 789
        </li>
        <li>
          <svg viewBox="0 0 24 24"><path d="M2 5h20v14H2z M2 5l10 8 10-8" /></svg>
          info@yourgmail.com
        </li>
        <li>
          <svg viewBox="0 0 24 24"><circle cx="12" cy="12" r="10"/></svg>
          www.yourwebsite.com
        </li>
      </ul>
    </div>

    <div class="services">
      <p class="services-title">Services I offer</p>
      <p class="services-list">Breakdowns, Field Service, A/C Systems, Machine rewires, Mine site vehicle fit outs</p>
    </div>
  </section>
</body>
</html>
```